pvt business card

need clean and modern business card design, possibly two. Logo on front and writing on back-Full source files for logo attached-THE CHOSEN LOGO IS SQUARE PVT with PVT HOLDINGS in ALL BLUE. Please do not use any other logos from files, this is source file that includes correct logo

```html
<!DOCTYPE html>
<html lang="en">
<head>
<meta charset="utf-8">
<title>PVT Holdings Business Card</title>
<link rel="stylesheet" href="https://fonts.googleapis.com/css2?family=Arimo:wght@400&family=Exo+2:wght@500&display=swap">
<style>
  :root {
    --backdrop: #162a3c;
    --brand-blue: #377bbf;
    --paper: #ffffff;
    --card-shadow: rgba(5, 12, 20, 0.55);
  }
  * { margin: 0; padding: 0; box-sizing: border-box; }
  html, body {
    width: 1200px;
    height: 1200px;
    overflow: hidden;
    background: var(--backdrop);
  }
  .canvas {
    position: relative;
    width: 1200px;
    height: 1200px;
  }
  .card {
    position: absolute;
    width: 549px;
    height: 323px;
    overflow: hidden;
    box-shadow: 6px 10px 18px var(--card-shadow);
  }
  /* Front */
  .card-front {
    left: 367px;
    top: 237px;
    background: var(--brand-blue);
  }
  .front-band {
    position: absolute;
    left: 175px;
    top: 0;
    width: 198px;
    height: 100%;
    background: var(--paper);
  }
  .front-square {
    position: absolute;
    left: 22px;
    top: 63px;
    width: 160px;
    height: 158px;
    background: var(--brand-blue);
  }
  .company-name {
    font-family: "Exo 2", sans-serif;
    font-weight: 500;
    white-space: nowrap;
    position: absolute;
    text-align: center;
  }
  .front-band .company-name {
    left: 0;
    width: 100%;
    top: 232px;
    font-size: 20px;
    letter-spacing: 3.4px;
    color: var(--brand-blue);
  }
  /* Back */
  .card-back {
    left: 373px;
    top: 625px;
    background: var(--paper);
  }
  .back-panel {
    position: absolute;
    left: 0;
    top: 0;
    width: 257px;
    height: 100%;
    background: var(--brand-blue);
  }
  .person-name {
    position: absolute;
    left: 36px;
    top: 64px;
    font-family: "Arimo", sans-serif;
    font-size: 36px;
    font-weight: 400;
    color: var(--paper);
    white-space: nowrap;
  }
  .back-square {
    position: absolute;
    left: 109px;
    top: 231px;
    width: 44px;
    height: 42px;
    background: var(--paper);
  }
  .back-panel .company-name {
    left: 0;
    width: 262px;
    top: 280px;
    font-size: 18px;
    letter-spacing: 3px;
    color: var(--paper);
  }
  .contact {
    position: absolute;
    right: 38px;
    top: 159px;
    text-align: right;
    font-family: "Arimo", sans-serif;
    color: var(--brand-blue);
    line-height: 1.2;
  }
  .contact .email { font-size: 15px; }
  .contact .web { font-size: 14px; }
</style>
</head>
<body>
<main class="canvas">
  <section class="card card-front" aria-label="Card front">
    <div class="front-band">
      <div class="front-square"></div>
      <p class="company-name">PVT HOLDINGS</p>
    </div>
  </section>

  <section class="card card-back" aria-label="Card back">
    <div class="back-panel">
      <p class="person-name">Owen Carter</p>
      <div class="back-square"></div>
      <p class="company-name">PVT HOLDINGS</p>
    </div>
    <div class="contact">
      <p class="email">contact@pvtholdings.com</p>
      <p class="web">www.pvtholdings.com</p>
    </div>
  </section>
</main>
</body>
</html>
```